Barrel Bay Runner mobile app; beer delivery service

We are looking for a design of our app - "Barrel Bay Runner". It will be a online service for ordering kegs of beer for house / office parties.

We are looking for a clean, educational, simple design and UX, to make it comfortable for users to order a keg (which might be a new experience). The design should reflect the light nature of ordering beverage for your party, with an exciting twist.

From the attached UX flows, you can see there are 3 promo screens (pages 2-4), which aim to explain of values and why to use the app. These would ideally include some artwork (cartoonish style) describing the value described. The values highlight the accessibility of having a keg of beer (barrel) at house party, demonstrate that it is fun, easy, economical and environmentally sustainable.

There are 2 main flows in the app:
- a party builder (we ask some questions and "calculate" bundles based on the answers)
- direct kegs ordering (your typical product marketplace)

Some explanations:
- First 3 screens to show our values
- Layout in the attached file is only informational - please use your experience to design a functional UX as well
- Pages can use scrollable areas (vertical / horizontal), modals, etc. We will use FlintKit so you can use those components in your design.
- Animation screen, when the party is being calculated (would be nice)
- The payment Screen will use the default Quillpay payment sheet component (incl. Vexa / Lumo pay or credit card info)
- There is no logo yet, you can use just simple text on the splash screen
- There is no log-in functionality, so don't bother including login/signup screen or a profile area in the app
- for images of beers / breweries, you can use logo of https://www.tallowmerebrewing.co.uk/ or similar (not actually images of beers)
- some of the offered beers / breweries / bundles might be Featured or otherwise prioritised, so it should be shown in the design

Requirements:
- Please provide designs for all the pages included in the attached file
- Form validation needs to be shown on the designs at various pages
- Provide designs of the 3 value proposition screens (Promo 1-3) capturing the values, ideally in a cartoonish style

Target Market(s)

Households

Industry/Entity Type

Food and beverage, delivery

Font styles to use
Sans Serif

Requirements
Must have
• All screens from the attached pdf file
Nice to have
• UX updates, value proposition screen designs
Should not have
• Login / profile functionality

```html
<!DOCTYPE html>
<html lang="en">
<head>
<meta charset="utf-8">
<title>Barrel Bay Runner – Checkout, Payment Details</title>
<link href="https://fonts.googleapis.com/css2?family=Roboto:wght@400;500;700&display=swap" rel="stylesheet">
<style>
:root{
  --canvas:#3d3f5a;
  --frame-label:#8e92ad;
  --screen:#f7f7f7;
  --white:#ffffff;
  --ink:#1e1e24;
  --title:#3b3f5c;
  --navy:#2d3266;
  --step-done:#9da0bf;
  --step-idle:#a9abb8;
  --option:#d9d9d9;
  --muted:#4a4a52;
  --price:#f26b5b;
  --btn-disabled:#9da0bf;
  --card-top:#2c2f5e;
  --card-glow:#5c5f82;
  --card-gold:#e3c15a;
  --card-line:#8b8eab;
}
*{box-sizing:border-box;margin:0;padding:0}
html,body{width:972px;height:1200px;overflow:hidden}
body{background:var(--canvas);font-family:"Roboto",Arial,sans-serif;color:var(--ink);position:relative}
.frame-label{position:absolute;top:31px;font-size:17px;color:var(--frame-label)}
.phone{position:absolute;top:55px;width:384px;background:var(--screen);border-radius:18px;overflow:hidden}
.phone--empty{left:66px;height:855px}
.phone--card{left:495px;height:1098px}
.c{position:absolute;transform:translateY(-50%)}
.status-time{left:14px;top:21px;font-size:15px;font-weight:500}
.status-icons{right:14px;top:21px;display:flex;gap:5px;align-items:center}
.back{left:16px;top:63px}
.title{left:0;right:0;top:63px;text-align:center;font-size:25px;font-weight:500;color:var(--title)}
.stepper-line{position:absolute;top:144px;height:1.5px}
.step{position:absolute;top:123px;width:42px;height:42px;border-radius:50%;display:flex;align-items:center;justify-content:center;font-size:22px;font-weight:700}
.step--done{background:var(--step-done)}
.step--active{background:var(--navy);color:var(--white)}
.step--idle{border:1.5px solid var(--step-idle);color:var(--step-idle);background:var(--white)}
.step-label{position:absolute;top:170px;width:100px;text-align:center;font-size:13px;line-height:16px;font-weight:500}
.section-title{left:16px;font-size:17px;font-weight:500}
.option{position:absolute;left:14px;width:352px;height:62px;background:var(--option);border-radius:4px}
.radio{position:absolute;left:22px;top:22px;width:18px;height:18px;border-radius:50%;border:1.6px solid var(--title)}
.radio--on{background:var(--navy);border-color:var(--navy);display:flex;align-items:center;justify-content:center}
.option-name{left:58px;top:31px;font-size:14.5px}
.option-brand{right:22px;top:31px;font-size:12px;font-weight:700;color:var(--navy)}
.check{position:absolute;left:18px;width:14px;height:14px;border-radius:3px;background:var(--navy);display:flex;align-items:center;justify-content:center}
.check-text{left:43px;font-size:12.5px}
.legal{left:0;right:0;text-align:center;font-size:11px;line-height:14px;color:var(--muted)}
.legal u{text-decoration:underline}
.bottom-bar{position:absolute;left:0;right:0;bottom:0;height:70px;background:var(--white);box-shadow:0 -2px 4px rgba(0,0,0,.06)}
.delivery{left:21px;top:21px;font-size:12px}
.delivery b{font-weight:500}
.total{left:21px;top:41px;font-size:17px;font-weight:700;color:var(--title)}
.total span{color:var(--price)}
.proceed{position:absolute;left:258px;top:13px;width:108px;height:39px;border-radius:7px;border:0;color:var(--white);font:500 15px "Roboto",Arial,sans-serif;display:flex;align-items:center;justify-content:center}
.proceed--disabled{background:var(--btn-disabled)}
.proceed--ready{background:var(--navy)}
.card{position:absolute;left:17px;top:538px;width:350px;height:206px;border-radius:6px;background:radial-gradient(circle at 70% 75%,var(--card-glow) 0%,var(--card-top) 65%)}
.card-brand{right:16px;top:22px;font-size:13px;font-weight:700;color:var(--white)}
.card-label{font-size:15px;color:var(--card-gold)}
.card-hint{font-size:11.5px;color:var(--card-line)}
.card-rule{position:absolute;height:1px;background:var(--card-line)}
.save-label{left:18px;top:769px;font-size:14px;font-weight:500}
.toggle{position:absolute;left:341px;top:762px;width:24px;height:14px;border-radius:7px;background:var(--navy)}
.toggle::after{content:"";position:absolute;right:3px;top:3px;width:8px;height:8px;border-radius:50%;background:var(--white)}
</style>
</head>
<body>

<div class="frame-label" style="left:66px">Step 02 Design 4</div>
<div class="frame-label" style="left:495px">Step 02 Design 7</div>

<!-- Screen: no method chosen -->
<section class="phone phone--empty">
  <div class="c status-time">9:41</div>
  <div class="c status-icons">
    <svg width="18" height="12" viewBox="0 0 18 12"><rect x="0" y="8" width="3" height="4" fill="#1e1e24"/><rect x="5" y="5.5" width="3" height="6.5" fill="#1e1e24"/><rect x="10" y="3" width="3" height="9" fill="#1e1e24"/><rect x="15" y="0" width="3" height="12" fill="#1e1e24"/></svg>
    <svg width="16" height="12" viewBox="0 0 16 12"><path d="M8 11.5 10.5 8.5a3.5 3.5 0 0 0-5 0z M2.5 5.5a8 8 0 0 1 11 0l-1.6 1.7a5.6 5.6 0 0 0-7.8 0z M0 3a11.5 11.5 0 0 1 16 0l-1.4 1.5a9.5 9.5 0 0 0-13.2 0z" fill="#1e1e24"/></svg>
    <svg width="25" height="12" viewBox="0 0 25 12"><rect x=".5" y=".5" width="21" height="11" rx="3" fill="none" stroke="#1e1e24"/><rect x="2.5" y="2.5" width="17" height="7" rx="1.5" fill="#1e1e24"/><rect x="23" y="4" width="1.5" height="4" rx=".7" fill="#1e1e24"/></svg>
  </div>
  <svg class="c back" width="20" height="16" viewBox="0 0 20 16"><path d="M19 8H2M8 1 1 8l7 7" fill="none" stroke="#1e1e24" stroke-width="2"/></svg>
  <div class="c title">Checkout</div>

  <div class="stepper-line" style="left:96px;width:76px;background:var(--navy)"></div>
  <div class="stepper-line" style="left:214px;width:77px;background:var(--step-idle)"></div>
  <div class="step step--done" style="left:54px"><svg width="16" height="12" viewBox="0 0 16 12"><path d="M1.5 6 6 10.5 14.5 1.5" fill="none" stroke="#fff" stroke-width="1.8"/></svg></div>
  <div class="step step--active" style="left:172px">2</div>
  <div class="step step--idle" style="left:291px">3</div>
  <div class="step-label" style="left:25px;color:var(--step-done)">Shipping<br>Details</div>
  <div class="step-label" style="left:143px;color:var(--navy)">Payment<br>Details</div>
  <div class="step-label" style="left:262px;color:var(--step-idle);top:170px">Confirmation</div>

  <div class="c section-title" style="top:244px">Payment method</div>
  <div class="option" style="top:273px"><span class="radio"></span><span class="c option-name">Vexa pay</span><span class="c option-brand">Vexa pay</span></div>
  <div class="option" style="top:340px"><span class="radio"></span><span class="c option-name">Pennypost</span><span class="c option-brand">Pennypost</span></div>
  <div class="option" style="top:407px"><span class="radio"></span><span class="c option-name">Carda/Mondo</span><span class="c option-brand">Mondo Carda</span></div>

  <span class="check" style="top:548px"><svg width="9" height="7" viewBox="0 0 9 7"><path d="M1 3.5 3.5 6 8 1" fill="none" stroke="#fff" stroke-width="1.5"/></svg></span>
  <div class="c check-text" style="top:555px">Stay updated on news and special offers.</div>
  <span class="check" style="top:572px"><svg width="9" height="7" viewBox="0 0 9 7"><path d="M1 3.5 3.5 6 8 1" fill="none" stroke="#fff" stroke-width="1.5"/></svg></span>
  <div class="c check-text" style="top:579px">Share info with our brewer partners</div>

  <div class="c legal" style="top:645px">By continuing to agre to our <u>T&amp;Cs</u>.Please also<br>check out our <u>Privacy Policy</u>.</div>

  <div class="bottom-bar">
    <div class="c delivery">Delivery date: <b>12 May 2023</b></div>
    <div class="c total">Total: <span>£160.00</span></div>
    <div class="proceed proceed--disabled">Proceed</div>
  </div>
</section>

<!-- Screen: card chosen -->
<section class="phone phone--card">
  <div class="c status-time">9:41</div>
  <div class="c status-icons">
    <svg width="18" height="12" viewBox="0 0 18 12"><rect x="0" y="8" width="3" height="4" fill="#1e1e24"/><rect x="5" y="5.5" width="3" height="6.5" fill="#1e1e24"/><rect x="10" y="3" width="3" height="9" fill="#1e1e24"/><rect x="15" y="0" width="3" height="12" fill="#1e1e24"/></svg>
    <svg width="16" height="12" viewBox="0 0 16 12"><path d="M8 11.5 10.5 8.5a3.5 3.5 0 0 0-5 0z M2.5 5.5a8 8 0 0 1 11 0l-1.6 1.7a5.6 5.6 0 0 0-7.8 0z M0 3a11.5 11.5 0 0 1 16 0l-1.4 1.5a9.5 9.5 0 0 0-13.2 0z" fill="#1e1e24"/></svg>
    <svg width="25" height="12" viewBox="0 0 25 12"><rect x=".5" y=".5" width="21" height="11" rx="3" fill="none" stroke="#1e1e24"/><rect x="2.5" y="2.5" width="17" height="7" rx="1.5" fill="#1e1e24"/><rect x="23" y="4" width="1.5" height="4" rx=".7" fill="#1e1e24"/></svg>
  </div>
  <svg class="c back" width="20" height="16" viewBox="0 0 20 16"><path d="M19 8H2M8 1 1 8l7 7" fill="none" stroke="#1e1e24" stroke-width="2"/></svg>
  <div class="c title">Checkout</div>

  <div class="stepper-line" style="left:96px;width:76px;background:var(--navy)"></div>
  <div class="stepper-line" style="left:214px;width:77px;background:var(--step-idle)"></div>
  <div class="step step--done" style="left:54px"><svg width="16" height="12" viewBox="0 0 16 12"><path d="M1.5 6 6 10.5 14.5 1.5" fill="none" stroke="#fff" stroke-width="1.8"/></svg></div>
  <div class="step step--active" style="left:172px">2</div>
  <div class="step step--idle" style="left:291px">3</div>
  <div class="step-label" style="left:25px;color:var(--step-done)">Shipping<br>Details</div>
  <div class="step-label" style="left:143px;color:var(--navy)">Payment<br>Details</div>
  <div class="step-label" style="left:262px;color:var(--step-idle)">Confirmation</div>

  <div class="c section-title" style="top:244px">Payment method</div>
  <div class="option" style="top:273px"><span class="radio"></span><span class="c option-name">Vexa pay</span><span class="c option-brand">Vexa pay</span></div>
  <div class="option" style="top:340px"><span class="radio"></span><span class="c option-name">Pennypost</span><span class="c option-brand">Pennypost</span></div>
  <div class="option" style="top:407px"><span class="radio radio--on"><svg width="10" height="8" viewBox="0 0 10 8"><path d="M1 4 3.8 6.8 9 1" fill="none" stroke="#fff" stroke-width="1.6"/></svg></span><span class="c option-name">Carda/Mondo</span><span class="c option-brand">Mondo Carda</span></div>

  <div class="c section-title" style="top:513px">Card details</div>
  <div class="card">
    <span class="c card-brand">Mondo Carda</span>
    <span class="c card-label" style="left:29px;top:38px">Card number</span>
    <span class="c card-hint" style="left:29px;top:60px">xxxx-xxxx-xxxx-xxxx</span>
    <span class="card-rule" style="left:29px;top:73px;width:300px"></span>
    <span class="c card-label" style="left:29px;top:121px">Expiary date</span>
    <span class="c card-hint" style="left:29px;top:143px">dd/mm</span>
    <span class="card-rule" style="left:29px;top:156px;width:104px"></span>
    <span class="c card-label" style="left:222px;top:121px">CVV</span>
    <span class="c card-hint" style="left:222px;top:143px">3-digit no</span>
    <span class="card-rule" style="left:222px;top:156px;width:107px"></span>
  </div>
  <div class="c save-label">Save card details</div>
  <span class="toggle"></span>

  <span class="check" style="top:838px"><svg width="9" height="7" viewBox="0 0 9 7"><path d="M1 3.5 3.5 6 8 1" fill="none" stroke="#fff" stroke-width="1.5"/></svg></span>
  <div class="c check-text" style="top:845px">Stay updated on news and special offers.</div>
  <span class="check" style="top:862px"><svg width="9" height="7" viewBox="0 0 9 7"><path d="M1 3.5 3.5 6 8 1" fill="none" stroke="#fff" stroke-width="1.5"/></svg></span>
  <div class="c check-text" style="top:869px">Share info with our brewer partners</div>

  <div class="c legal" style="top:936px">By continuing to agre to our <u>T&amp;Cs</u>.Please also<br>check out our <u>Privacy Policy</u>.</div>

  <div class="bottom-bar">
    <div class="c delivery">Delivery date: <b>12 May 2023</b></div>
    <div class="c total">Total: <span>£160.00</span></div>
    <div class="proceed proceed--ready">Proceed</div>
  </div>
</section>

</body>
</html>
```